Web form face-lift for an online startup

We are a web startup building a SaaS application for the freight industry. The project is mainly dedicated to the paint the main form that our customer are using along the search results that the they get. All details are in the attached documents.
Updates
The application serves the Freight Forwarders community so please think towards this industry when using background images, banners, colors, icons, etc. Computer and technology images are irrelevant.
Customer fields at the top of the page is actually part of the form.
Target Market(s)
Usually business users (Sales people, procurement, shippers, freight forwarders). Some are less tech savvy and some appreciate the new trendy web apps.
Industry/Entity Type
Building
Colors
Designer to choose colors to be used in the design.
Look and feel
Each slider illustrates characteristics of the customer's brand and the style your logo design should communicate.

```html
<!DOCTYPE html>
<html lang="en">
<head>
<meta charset="utf-8">
<title>Quovira Forms – Search for Quotes</title>
<link href="https://fonts.googleapis.com/css2?family=Open+Sans:wght@400;600&family=Ubuntu:wght@300;400;500&display=swap" rel="stylesheet">
<style>
:root{
  --red:#d9493a;
  --red-dark:#b83a2d;
  --green:#8cc152;
  --green-dark:#73a83f;
  --ink:#555;
  --muted:#888;
  --field:#d4d4d4;
  --field-border:#bcbcbc;
  --page:#f6f6f6;
  --header:#f0f0f0;
  --footer:#2b2b2b;
  --white:#fff;
}
*{box-sizing:border-box;margin:0;padding:0}
html,body{width:1200px;height:1114px;overflow:hidden}
body{position:relative;background:var(--page);font-family:"Open Sans",Arial,sans-serif;font-size:13px;color:var(--ink)}
.abs{position:absolute;white-space:nowrap}

/* top bar */
.topbar{left:0;top:0;width:1200px;height:50px;background:var(--white);border-bottom:1px solid #e4e4e4}
.caret{display:inline-block;width:0;height:0;border-left:4px solid transparent;border-right:4px solid transparent;border-top:5px solid #333;vertical-align:middle;margin-left:5px}
.lang{left:867px;top:16px;color:#333}
.user{left:958px;top:16px;color:#7a3a14}
.avatar{left:1050px;top:5px;width:40px;height:40px;border-radius:50%;background:linear-gradient(160deg,#c9c9c9,#6c6c6c)}
.avatar-status{left:1080px;top:35px;width:9px;height:9px;border-radius:50%;background:#4cc04c;border:1px solid #fff}

/* header */
.header{left:0;top:50px;width:1200px;height:83px;background:var(--header)}
.brand{left:110px;top:72px;font-family:"Ubuntu",sans-serif;font-size:34px;font-weight:300;color:#8a8a8a;line-height:44px}
.nav-item{top:85px;font-size:13.5px;color:#888}
.nav-item.active{color:var(--red)}

/* hero */
.hero{left:0;top:133px;width:1200px;height:433px;background:radial-gradient(ellipse at 70% 75%,#4a4130 0%,#231f17 35%,#0d0c0a 75%),#0d0c0a}
.hero-title{left:111px;top:284px;font-family:"Ubuntu",sans-serif;font-size:23px;font-weight:400;color:var(--white)}
.customer-input{left:110px;top:319px;width:318px;height:38px;background:#dcdcdc;border:1px solid #bbb;padding:0 7px;font-size:12px;font-style:italic;color:#999;line-height:36px}
.rate{left:110px;top:364px;font-size:13px;color:var(--red)}
.checkbox{display:inline-block;width:12px;height:12px;border:1px solid #999;background:#fff;vertical-align:middle}
.rate svg{vertical-align:middle;position:relative;top:-2px;margin-right:2px}

/* tabs */
.tab{background:#dedede;color:#555;font-size:14px;font-weight:600;text-align:center;line-height:39px}
.tab-active{left:323px;top:488px;width:178px;height:78px;background:var(--white);border-top:2px solid #ddd}
.tab-active .box-art{position:absolute;left:7px;top:10px;width:70px;height:56px;background:linear-gradient(#e6b58e,#c98757)}
.tab-active .label{position:absolute;left:93px;top:21px;font-size:13.5px;font-weight:600;color:#555;line-height:17px}
.tab-container{left:511px;top:527px;width:178px;height:39px}
.tab-parcel{left:699px;top:527px;width:178px;height:39px}
.more{left:887px;top:540px;font-size:11px;color:#bbb}

/* form */
.lbl{font-size:13px;color:#777}
.field{height:22px;background:var(--field);border:1px solid var(--field-border);font-size:13px;color:#666;text-align:center;line-height:20px}
.field.white{background:#fff;border-color:#ccc}
.unit{height:22px;background:var(--red);color:#fff;font-size:13px;line-height:21px;padding-left:13px}
.unit::after{content:"";position:absolute;right:3px;top:3px;width:15px;height:15px;background:#f4f4f4;border:1px solid #999}
.unit i,.select i{position:absolute;right:7px;top:9px;width:0;height:0;border-left:4px solid transparent;border-right:4px solid transparent;border-top:5px solid #333;z-index:1}
.select{height:22px;background:var(--field);border:1px solid #aaa;color:#999;font-size:11px;padding-left:6px;line-height:20px}
.select::after{content:"";position:absolute;right:3px;top:3px;width:15px;height:15px;background:#f4f4f4;border:1px solid #888}
.btn-add{left:112px;top:655px;width:124px;height:34px;background:var(--red);border-bottom:2px solid var(--red-dark);color:#fff;font-size:12.5px;text-align:center;line-height:32px}
.band{left:110px;width:990px;height:60px;background:#fbfbfb;box-shadow:0 6px 8px -8px rgba(0,0,0,.25),0 -6px 8px -8px rgba(0,0,0,.2)}
.addr{height:31px;background:var(--field);border:1px solid #bbb;font-size:12.5px;color:#777;padding-left:9px;line-height:29px}
.options-title{left:110px;top:877px;font-family:"Ubuntu",sans-serif;font-size:16px;font-weight:400;color:#333}
.radio{display:inline-block;width:12px;height:12px;border-radius:50%;border:1px solid #aaa;background:#eee;vertical-align:middle;margin-right:2px;position:relative;top:-1px}
.opt{top:913px;font-size:13px;color:#888}
.incoterm b{color:var(--red);font-weight:600}
.ico{display:inline-block;vertical-align:middle;margin-left:5px}
.more-opt{left:1020px;top:944px;font-size:11px;color:#777}
.btn{top:977px;height:44px;color:#fff;font-family:"Ubuntu",sans-serif;font-size:17px;font-weight:500;text-align:center;line-height:42px}
.btn-search{left:392px;width:187px;background:var(--red);border-bottom:3px solid var(--red-dark)}
.btn-create{left:621px;width:187px;background:var(--green);border-bottom:3px solid var(--green-dark)}
.or{left:590px;top:990px;font-size:13px;color:#888}

/* footer */
.footer{left:0;top:1063px;width:1200px;height:51px;background:var(--footer)}
.footer-link{top:1082px;font-size:12px;color:#999}
</style>
</head>
<body>

<div class="abs topbar"></div>
<div class="abs" style="left:805px;top:15px">
  <svg width="30" height="20" viewBox="0 0 30 20"><circle cx="9" cy="10" r="8" fill="none" stroke="#222" stroke-width="1.8"/><text x="9" y="14" font-size="11" text-anchor="middle" font-family="Open Sans,sans-serif" font-weight="600" fill="#222">$</text><path d="M22 9h7l-3.5 4z" fill="#222"/></svg>
</div>
<div class="abs lang">English<span class="caret"></span></div>
<div class="abs user">Mark.Ellis<span class="caret"></span></div>
<div class="abs avatar" role="img" aria-label="User profile photo"></div>
<div class="abs avatar-status"></div>

<div class="abs header"></div>
<div class="abs brand">Quovira Forms</div>
<span class="abs nav-item active" style="left:553px">HOME</span>
<span class="abs nav-item" style="left:617px">Menu Item1</span>
<span class="abs nav-item" style="left:716px">Menu Item2</span>
<span class="abs nav-item" style="left:815px">Menu Item3</span>
<span class="abs nav-item" style="left:914px">Menu Item4</span>
<span class="abs nav-item" style="left:1013px">Menu Item5</span>

<div class="abs hero" role="img" aria-label="Dusk photograph of a motorway with lorries driving through wooded hills"></div>
<h1 class="abs hero-title">Search for Quotes</h1>
<div class="abs customer-input">Customer Name..</div>
<div class="abs rate"><svg width="13" height="13" viewBox="0 0 13 13"><rect x=".5" y=".5" width="12" height="12" fill="#fff" stroke="#999"/><path d="M3 6.5l2.5 2.5L10 3.5" fill="none" stroke="#1a9a8a" stroke-width="2"/></svg>Rate quote?</div>

<div class="abs tab-active">
  <div class="box-art" role="img" aria-label="Open cardboard box illustration"></div>
  <div class="label">BOX<br>OR PALLET</div>
</div>
<div class="abs tab tab-container">SHIPPING CONTAINER</div>
<div class="abs tab tab-parcel">ENVELOPE OR PARCEL</div>
<div class="abs more">MORE »</div>

<div class="abs lbl" style="left:115px;top:589px">QTY</div>
<div class="abs lbl" style="left:215px;top:589px">Stackabel</div>
<div class="abs lbl" style="left:337px;top:589px">Load</div>
<div class="abs lbl" style="left:651px;top:589px">lenght</div>
<div class="abs lbl" style="left:731px;top:589px">Width</div>
<div class="abs lbl" style="left:805px;top:589px">Height</div>
<div class="abs lbl" style="left:956px;top:589px">Weight</div>

<div class="abs field" style="left:112px;top:618px;width:39px">05</div>
<span class="abs checkbox" style="left:236px;top:621px"></span>
<div class="abs select" style="left:337px;top:619px;width:210px">Box/Pallet<i></i></div>
<div class="abs field" style="left:644px;top:618px;width:59px">100</div>
<div class="abs field" style="left:721px;top:618px;width:59px">100</div>
<div class="abs field" style="left:797px;top:618px;width:59px">100</div>
<div class="abs unit" style="left:867px;top:618px;width:69px">cm<i></i></div>
<div class="abs field" style="left:948px;top:618px;width:60px">100</div>
<div class="abs unit" style="left:1019px;top:618px;width:69px">kg<i></i></div>

<div class="abs btn-add">+ Add more units</div>

<div class="abs band" style="top:710px"></div>
<div class="abs lbl" style="left:727px;top:733px">Total</div>
<div class="abs field white" style="left:761px;top:730px;width:59px">05</div>
<div class="abs field white" style="left:826px;top:730px;width:50px">01</div>
<div class="abs unit" style="left:876px;top:730px;width:69px">cm<i></i></div>
<div class="abs field white" style="left:970px;top:730px;width:50px">100</div>
<div class="abs unit" style="left:1020px;top:730px;width:69px">kg<i></i></div>

<div class="abs lbl" style="left:109px;top:803px">From:</div>
<div class="abs addr" style="left:150px;top:796px;width:344px">Shipping address or port</div>
<div class="abs lbl" style="left:720px;top:803px">To:</div>
<div class="abs addr" style="left:747px;top:796px;width:344px">Shipping address or port</div>

<h2 class="abs options-title">Options</h2>
<div class="abs opt" style="left:110px"><span class="radio"></span>Import</div>
<div class="abs opt" style="left:204px"><span class="radio"></span>Export</div>
<div class="abs opt incoterm" style="left:306px">Incoterm: <b>FCA</b></div>
<div class="abs opt" style="left:525px;top:910px"><span class="checkbox"></span><svg class="ico" width="18" height="18" viewBox="0 0 18 18"><circle cx="9" cy="9" r="8" fill="#fff" stroke="#e08a80" stroke-width="1.5"/><path d="M6 12l6-6M7 6h4v4" fill="none" stroke="#999" stroke-width="1.5"/></svg></div>
<div class="abs opt" style="left:584px;top:910px"><span class="checkbox"></span><svg class="ico" width="18" height="18" viewBox="0 0 18 18"><circle cx="9" cy="9" r="8" fill="#fff" stroke="#e08a80" stroke-width="1.5"/><circle cx="9" cy="7" r="2.5" fill="#999"/><path d="M4.5 14a4.5 4 0 0 1 9 0z" fill="#999"/></svg></div>
<div class="abs opt" style="left:641px;top:910px"><span class="checkbox"></span><svg class="ico" width="18" height="18" viewBox="0 0 18 18"><circle cx="9" cy="9" r="8" fill="#fff" stroke="#e08a80" stroke-width="1.5"/><path d="M5 5l8 8M13 5l-8 8" stroke="#e08a80" stroke-width="2"/></svg></div>
<div class="abs select" style="left:861px;top:912px;width:229px;color:#555">Price level<i></i></div>
<div class="abs more-opt">More options</div>

<div class="abs btn btn-search">SEARCH QUOTES</div>
<div class="abs or">OR</div>
<div class="abs btn btn-create">CREATE MANUALLY</div>

<footer class="abs footer"></footer>
<span class="abs footer-link" style="left:112px">About us</span>
<span class="abs footer-link" style="left:173px">Privacy policy</span>
<span class="abs footer-link" style="left:265px">Terms of service</span>
<span class="abs footer-link" style="left:372px">News</span>
<span class="abs footer-link" style="left:805px">Blog</span>
<span class="abs footer-link" style="left:843px">Friendbook</span>
<span class="abs footer-link" style="left:918px">Chirper</span>
<span class="abs footer-link" style="left:972px">Worklink</span>
<span class="abs footer-link" style="left:1034px">ViewTube</span>

</body>
</html>
```